Refresh of The Marston Collective business card

Update business card design using existing primary logo. Names, numbers, etc. are too hard to read on current design.

Target Market(s)

We are a CPA firm.

Industry/Entity Type

Accountant

Contact Information for Business Card

update current card

Colors
0355a3
3176b5
85acd3
0792cd

Requirements
Must have
• Easier to read phone numbers and names
• Use existing logo
Nice to have
• We love our color scheme and current TMC logo. But the names and phone numbers are too small and card just look old and stale.

```html
<!DOCTYPE html>
<html lang="en">
<head>
<meta charset="utf-8">
<title>The Marston Collective — Business Card</title>
<link rel="stylesheet" href="https://fonts.googleapis.com/css2?family=Cinzel:wght@600&family=Questrial&display=swap">
<style>
  :root {
    --navy: #0355a3;
    --mid-blue: #3176b5;
    --light-blue: #85acd3;
    --bright-blue: #0792cd;
    --ink: #1a1a1a;
    --paper: #ffffff;
    --backdrop: #e4e4e4;
  }
  * { box-sizing: border-box; margin: 0; padding: 0; }
  html, body {
    width: 1200px; height: 1000px; overflow: hidden;
    background: var(--backdrop);
  }
  .canvas { position: relative; width: 1200px; height: 1000px; }

  .card {
    position: absolute; left: 250px; width: 700px; height: 400px;
    overflow: hidden; box-shadow: 0 6px 18px rgba(0,0,0,0.12);
  }

  /* Front of card */
  .card-front { top: 70px; background: var(--paper); }
  .band { position: absolute; left: 0; right: 0; background: linear-gradient(90deg, var(--mid-blue), var(--bright-blue)); }
  .band-top { top: 0; height: 22px; }
  .band-bottom { bottom: 0; height: 26px; }

  .brand-small {
    position: absolute; left: 34px; top: 48px;
    display: flex; align-items: center; gap: 10px;
  }
  .brand-dot { width: 34px; height: 34px; border-radius: 50%; background: var(--navy); }
  .brand-small-name {
    font-family: 'Cinzel', serif; font-weight: 600; font-size: 14px;
    color: var(--navy); letter-spacing: 0.5px;
  }

  .holder-name {
    position: absolute; left: 40px; top: 196px;
    font-family: 'Cinzel', serif; font-weight: 600; font-size: 25px;
    color: var(--ink); letter-spacing: 0.5px;
  }

  .contact-list {
    position: absolute; left: 400px; top: 84px; list-style: none;
    font-family: 'Questrial', sans-serif; font-size: 15px; color: var(--ink);
  }
  .contact-item { display: flex; align-items: flex-start; gap: 14px; margin-bottom: 16px; line-height: 1.3; }
  .contact-icon { width: 18px; height: 18px; flex: none; fill: var(--mid-blue); margin-top: 1px; }

  /* Back of card */
  .card-back {
    top: 530px;
    background: radial-gradient(ellipse at 50% 42%, #4fa6dc 0%, #2488c8 40%, #0a70b3 100%);
  }
  .brand-large {
    position: absolute; left: 130px; top: 120px;
    display: flex; align-items: center; gap: 28px;
  }
  .brand-ring { width: 128px; height: 128px; border-radius: 50%; border: 4px solid var(--paper); }
  .brand-large-text { display: flex; flex-direction: column; gap: 12px; }
  .brand-large-name {
    font-family: 'Cinzel', serif; font-weight: 600; font-size: 36px;
    color: var(--paper); line-height: 1.05;
  }
  .tagline {
    font-family: 'Questrial', sans-serif; font-size: 12px;
    letter-spacing: 3.5px; text-transform: uppercase; color: #d6e8f6;
  }
  .website {
    position: absolute; right: 110px; bottom: 78px;
    font-family: 'Questrial', sans-serif; font-size: 15px; font-weight: 700;
    color: var(--paper); letter-spacing: 0.5px;
  }
</style>
</head>
<body>
<main class="canvas">

  <section class="card card-front" aria-label="Card front">
    <div class="band band-top"></div>

    <div class="brand-small">
      <span class="brand-dot"></span>
      <span class="brand-small-name">The Marston Collective</span>
    </div>

    <p class="holder-name">Daniel R. Marston, CPA</p>

    <ul class="contact-list">
      <li class="contact-item">
        <svg class="contact-icon" viewBox="0 0 24 24" aria-hidden="true"><path d="M12 2a7 7 0 0 0-7 7c0 5 7 13 7 13s7-8 7-13a7 7 0 0 0-7-7zm0 9.5A2.5 2.5 0 1 1 12 6.5a2.5 2.5 0 0 1 0 5z"/></svg>
        <span>118 Linden Park Ave, Suite 310<br>Westbrook, Florida 32900</span>
      </li>
      <li class="contact-item">
        <svg class="contact-icon" viewBox="0 0 24 24" aria-hidden="true"><path d="M6.6 10.8a15 15 0 0 0 6.6 6.6l2.2-2.2a1 1 0 0 1 1-.25 11.4 11.4 0 0 0 3.6.57 1 1 0 0 1 1 1V20a1 1 0 0 1-1 1A17 17 0 0 1 3 4a1 1 0 0 1 1-1h3.5a1 1 0 0 1 1 1c0 1.25.2 2.45.57 3.6a1 1 0 0 1-.25 1z"/></svg>
        <span>555.204.3187</span>
      </li>
      <li class="contact-item">
        <svg class="contact-icon" viewBox="0 0 24 24" aria-hidden="true"><path d="M7 3h8v5H7zM4 9h16a1 1 0 0 1 1 1v9a1 1 0 0 1-1 1H4a1 1 0 0 1-1-1v-9a1 1 0 0 1 1-1zm3 4v2h10v-2z"/></svg>
        <span>555.204.3188</span>
      </li>
      <li class="contact-item">
        <svg class="contact-icon" viewBox="0 0 24 24" aria-hidden="true"><path d="M8 2h8a2 2 0 0 1 2 2v16a2 2 0 0 1-2 2H8a2 2 0 0 1-2-2V4a2 2 0 0 1 2-2zm0 3v12h8V5zm4 13.5a1 1 0 1 0 0 2 1 1 0 0 0 0-2z"/></svg>
        <span>555.204.3189</span>
      </li>
      <li class="contact-item">
        <svg class="contact-icon" viewBox="0 0 24 24" aria-hidden="true"><path d="M3 5h18a1 1 0 0 1 1 1v12a1 1 0 0 1-1 1H3a1 1 0 0 1-1-1V6a1 1 0 0 1 1-1zm1 2.3V17h16V7.3l-8 5.2z"/></svg>
        <span>dan@marstoncollective.com</span>
      </li>
    </ul>

    <div class="band band-bottom"></div>
  </section>

  <section class="card card-back" aria-label="Card back">
    <div class="brand-large">
      <span class="brand-ring"></span>
      <div class="brand-large-text">
        <span class="brand-large-name">The Marston<br>Collective</span>
        <span class="tagline">Certified Public Accountants</span>
      </div>
    </div>
    <p class="website">www.marstoncollective.com</p>
  </section>

</main>
</body>
</html>
```